I need a business logo and business card design for a new company in Alder Ridge, Vermont called 'Brightwell Clinic'. Brightwell Clinic is a primary care and walk-in clinic. The logo should have the letters 'BW' connected together. The letter 'F' should be navy blue and the letter 'C' should be orange. I have attached a several business cards and the logo should be simple and memorable. I like the Harrowgate Clinic font for my card. The card should have the simplicity of Harrowgate Clinic.

The logo should be on the upper left and the name 'Brightwell Clinic' should be next to the logo.

My name Dr. Tomas Lindqvist should be in the center of the card aligned left.
Dr. Tomas Lindqvist
Board Certified in Internal Medicine
Medical Director

The bottom left should have my address.
2917 Maple Hollow Court
Suite 4B
Alder Ridge, Vermont 22981

The bottom right should have my phone number and fax number.
Ph 555-014-2736
Fax 555-014-8490

The back of the card should have serve as an appointment reminder.
Appointment
For ____________________________________________
On _______________________at ___________________AM / PM
With ___________________________________________

If you are unable to keep your appointment, please give us 24 hour notice at 555-014-2736. Thank you.

```html
<!DOCTYPE html>
<html lang="en">
<head>
<meta charset="utf-8">
<title>Brightwell Clinic – Business Card</title>
<link rel="stylesheet" href="https://fonts.googleapis.com/css2?family=Open+Sans:wght@400;600&display=swap">
<style>
  :root {
    --band-blue: #3466b4;
    --navy: #2f4f8f;
    --orange: #f39a1e;
    --ink: #151515;
    --paper: #ffffff;
    --backdrop: #e9e6e1;
  }
  * { box-sizing: border-box; margin: 0; padding: 0; }
  html, body { width: 1200px; height: 858px; overflow: hidden; }
  body {
    background: var(--backdrop);
    font-family: "Open Sans", Arial, sans-serif;
    color: var(--ink);
    position: relative;
  }
  .card {
    position: absolute;
    top: 269px;
    width: 560px;
    height: 320px;
    background: var(--paper);
    box-shadow: 0 4px 14px rgba(0,0,0,0.18);
    overflow: hidden;
  }
  .card--front { left: 20px; }
  .card--back { left: 620px; }
  .card__band {
    position: absolute;
    top: 0;
    width: 24px;
    height: 100%;
    background: var(--band-blue);
  }
  .card__band--left { left: 0; }
  .card__band--right { right: 0; }

  /* Front */
  .brand {
    position: absolute;
    left: 56px;
    top: 40px;
    display: flex;
    align-items: center;
    gap: 10px;
  }
  .brand__mark {
    width: 18px;
    height: 18px;
    background: var(--orange);
  }
  .brand__name {
    font-size: 26px;
    font-weight: 400;
    color: var(--navy);
    letter-spacing: 0.2px;
  }
  .doctor {
    position: absolute;
    left: 56px;
    top: 118px;
  }
  .doctor__name {
    font-size: 27px;
    font-weight: 600;
    line-height: 1.15;
  }
  .doctor__role {
    font-size: 15px;
    line-height: 1.3;
  }
  .contact-phones {
    position: absolute;
    right: 44px;
    top: 118px;
    font-size: 19px;
    line-height: 1.45;
  }
  .contact-phones__row {
    display: flex;
    align-items: center;
    justify-content: flex-end;
    gap: 8px;
  }
  .icon {
    width: 14px;
    height: 14px;
    background: var(--band-blue);
    display: inline-flex;
    align-items: center;
    justify-content: center;
    flex: none;
  }
  .address {
    position: absolute;
    left: 56px;
    bottom: 30px;
    display: flex;
    gap: 10px;
    font-size: 19px;
    line-height: 1.2;
  }
  .address .icon { margin-top: 6px; }

  /* Back */
  .appointment__title {
    position: absolute;
    top: 38px;
    left: 0;
    width: 100%;
    text-align: center;
    font-size: 32px;
    font-weight: 600;
  }
  .appointment__form {
    position: absolute;
    left: 60px;
    right: 60px;
    top: 112px;
    font-size: 15px;
  }
  .form-row {
    display: flex;
    align-items: flex-end;
    gap: 6px;
    height: 30px;
  }
  .form-line {
    flex: 1;
    border-bottom: 2px dotted var(--ink);
    height: 16px;
  }
  .form-line--short { flex: 1.4; }
  .ampm {
    font-size: 11px;
    line-height: 1.1;
    text-align: left;
  }
  .appointment__note {
    position: absolute;
    left: 60px;
    right: 60px;
    bottom: 34px;
    font-size: 16px;
    line-height: 1.35;
  }
</style>
</head>
<body>

  <section class="card card--front" aria-label="Business card front">
    <div class="card__band card__band--left"></div>
    <div class="card__band card__band--right"></div>

    <div class="brand">
      <span class="brand__mark"></span>
      <span class="brand__name">Brightwell Clinic</span>
    </div>

    <div class="doctor">
      <p class="doctor__name">Dr. Tomas Lindqvist</p>
      <p class="doctor__role">Medical Director</p>
      <p class="doctor__role">Board Certified in Internal Medicine</p>
    </div>

    <div class="contact-phones">
      <div class="contact-phones__row">
        <span>555-014-2736</span>
        <span class="icon" aria-label="Phone">
          <svg width="10" height="10" viewBox="0 0 10 10"><path d="M2 1 L4 1 L4.6 3 L3.4 3.8 Q4.4 5.8 6.2 6.6 L7 5.4 L9 6 L9 8 Q8.5 9 7.5 9 Q1 8 1 2 Q1.2 1 2 1 Z" fill="#fff"/></svg>
        </span>
      </div>
      <div class="contact-phones__row">
        <span>555-014-8490</span>
        <span class="icon" aria-label="Fax">
          <svg width="10" height="10" viewBox="0 0 10 10"><rect x="2.5" y="1" width="5" height="3" fill="#fff"/><rect x="1" y="4" width="8" height="4" fill="#fff"/><rect x="2.5" y="6.5" width="5" height="2.5" fill="#3466b4" stroke="#fff" stroke-width="0.8"/></svg>
        </span>
      </div>
    </div>

    <div class="address">
      <span class="icon" aria-label="Location">
        <svg width="10" height="10" viewBox="0 0 10 10"><path d="M5 9.5 L2 5 A3.2 3.2 0 1 1 8 5 Z" fill="#fff"/><circle cx="5" cy="3.6" r="1.2" fill="#3466b4"/></svg>
      </span>
      <div>
        <p>2917 Maple Hollow Court</p>
        <p>Suite 4B</p>
        <p>Alder Ridge, Vermont 22981</p>
      </div>
    </div>
  </section>

  <section class="card card--back" aria-label="Business card back, appointment reminder">
    <div class="card__band card__band--left"></div>
    <div class="card__band card__band--right"></div>

    <h1 class="appointment__title">Appointment</h1>

    <div class="appointment__form">
      <div class="form-row"><span>For</span><span class="form-line"></span></div>
      <div class="form-row">
        <span>On</span><span class="form-line form-line--short"></span>
        <span>at</span><span class="form-line"></span>
        <span class="ampm">AM<br>PM</span>
      </div>
      <div class="form-row"><span>With</span><span class="form-line"></span></div>
    </div>

    <p class="appointment__note">If you are unable to keep your appointment, please give us 24 hour notice at 555-014-2736. Thank you.</p>
  </section>

</body>
</html>
```